Floor Plan Brochure (Pricing & Services) for Real Estate Agents

We are a company that help with the marketing properties for sale. It is a combined service where we Styling/Staging Properties & we also provided wide variety of Floor Plans for Real Estate Agents.

The focus is on our services of Floor Plans. I have attached a file and this will give you an idea of the services that we are trying to sell and also attached is a PDF of how I would like the brochure to be laid out / but again up to you on best design layout?? I am not looking for a repeat of this design (hence the reason for a new design). We would like something professional that will appeal to the high end estate agents and sell the service of floor plans.

Ideally we would like it to continue on with our theme of our website www.roomharbourly.com.au

Will require format in indesign and we can convert to PDF.
Updates

Hi!

As I am new to this, I really know what I was after or tell you what was required.

I have updated the brief and tried to help you as much as possible. Please review and please don't hesitate to ask a question if I haven't explained properly.

Cheers
Pip

Reason: Have provided more information, so designers know what we are looking for and hope it helps.

Target Market(s)

Real Estate Agents

Industry/Entity Type

Marketing

Requirements
Must have
• *A4 design layout and format in Indesign.

Front Page
*Must have front page that makes clients want to turn the page and instantly know what we are trying to sell. Floor Plans!
*with logo
*Want to achieve higher commission levels?

2nd Page
How floor plans will increase your commission

Follow on
upto you and layout.

*Must have lots of white space and only small proportion on green as pop colour, similar to first page on website.

*No boarders around pictures.

*Must include pricing and images of floor plans
Nice to have
• *On reflection would be nice to have Tri-fold layout. Just make it look good keep in mind that I would like the option to print as well as email to agents.
*Nice to have new header & footer or design layout.
*would be nice to sell each plan/service on an individual page and blurb and cost shown in a small proportion of white space. Maybe both site and floor plan on each page?
*would be nice to include script shown in attached PDF (the pricing & services that we offer, but can always cull wording depending on your design)

Should not have
• Please do not replicate the style/layout of what I have submitted in the PDF. I am looking for something professional to send to high end real estate agencies.

```html
<!DOCTYPE html>
<html lang="en">
<head>
<meta charset="utf-8">
<title>Tri-fold brochure option 2 set</title>
<link href="https://fonts.googleapis.com/css2?family=Arimo:wght@400;700&family=Open+Sans:wght@300;400&display=swap" rel="stylesheet">
<style>
:root{
  --stage:#6b7471;
  --paper:#ffffff;
  --green-dark:#6a8a3a;
  --green-mid:#8fae52;
  --green-light:#b5cf7e;
  --green-pale:#c9dc9c;
  --ink:#4a4a4a;
  --ink-soft:#666;
  --band-grey:#e6e6e6;
  --title-yellow:#f4e64a;
  --label:#f0f0f0;
}
*{margin:0;padding:0;box-sizing:border-box}
html,body{width:1200px;height:596px;overflow:hidden;background:var(--stage)}
body{position:relative;font-family:"Arimo",Arial,sans-serif;color:var(--ink)}
.set-title{position:absolute;top:12px;left:0;width:1200px;text-align:center;color:var(--title-yellow);font-size:14px}
.panel{position:absolute;top:34px;width:376px;height:527px;background:var(--paper);overflow:hidden;border-right:1px solid #333}
.panel-page5{left:37px}
.panel-back{left:413px}
.panel-cover{left:789px}
.page-label{position:absolute;top:572px;color:var(--label);font-size:14px;text-align:center;width:300px}

/* header */
.header-tab{position:absolute;top:29px;left:0;width:22px;height:32px;background:var(--green-light)}
.header-band{position:absolute;top:29px;left:22px;width:108px;height:32px;background:var(--green-dark)}
.header-num{position:absolute;top:22px;left:114px;font-size:44px;font-weight:700;color:#fff;line-height:1}
.header-title{position:absolute;top:31px;left:138px;font-size:22px;font-weight:700;color:var(--green-dark);line-height:1}
.header-sub{position:absolute;top:60px;left:138px;font-size:13px;font-weight:700;color:var(--ink-soft);line-height:1}

/* body copy */
.sec-head{position:absolute;font-size:6.6px;font-weight:700;color:var(--green-mid);text-transform:uppercase;line-height:1.3}
.sec-head.title-case{text-transform:none}
.copy{position:absolute;font-size:6.3px;line-height:1.6;color:var(--ink-soft)}
.price-list{position:absolute;font-size:6.1px;line-height:1.65;color:var(--green-light);list-style:none}
.large-homes{position:absolute;font-size:7px;font-weight:700;color:var(--ink-soft)}
.media{position:absolute}
.video-frame{position:absolute;left:264px;top:192px;width:79px;height:70px;background:#222;border-radius:3px;padding:4px 4px 12px}
.video-frame .media{position:static;width:100%;height:100%;background:linear-gradient(180deg,#9b8c7a,#d8cfc2 55%,#6e5b47)}
.hyper-note{position:absolute;left:253px;top:265px;width:102px;text-align:center;font-size:6.6px;font-weight:700;color:var(--green-dark);line-height:1.2}

.photo-strip{position:absolute;left:0;top:400px;width:376px;height:66px;background:linear-gradient(90deg,#7a6a58,#c8b9a4 30%,#e9e6e0 55%,#b9bcbf 80%,#8c8d8a)}
.footer-band{position:absolute;left:0;top:466px;width:376px;height:51px;background:var(--green-dark)}
.footer-url-box{position:absolute;left:0;top:472px;width:120px;height:20px;background:var(--green-light);color:#fff;font-size:6.4px;padding:7px 0 0 14px}
.footer-rule{position:absolute;left:208px;top:496px;width:168px;height:3px;background:#dde4cc}

/* back page */
.offer-band{position:absolute;left:0;top:275px;width:376px;height:32px;background:var(--band-grey);padding:7px 26px 0 28px;font-size:6.3px;font-weight:700;color:var(--green-mid);line-height:1.4}
.plan-link{position:absolute;left:0;top:314px;width:376px;text-align:center;font-size:6.6px;color:var(--ink)}
.book-cta{position:absolute;left:0;top:337px;width:376px;text-align:center;font-size:8.4px;font-weight:700;color:var(--green-dark);line-height:1.45}
.help-band{position:absolute;left:0;top:372px;width:376px;height:26px;background:var(--green-pale);color:#fff;font-size:7.6px;text-align:center;padding:9px 0 0 60px}
.phone-band{position:absolute;left:0;top:398px;width:376px;height:23px;background:var(--green-dark);color:#fff;font-size:10px;font-weight:700;text-align:center;padding-top:6px}
.brand{position:absolute;display:flex;align-items:center;gap:5px}
.brand-square{width:9px;height:9px;background:var(--green-light)}
.brand-name{font-size:15px;font-weight:700;color:var(--green-dark);letter-spacing:-.2px}
.brand-url{position:absolute;left:0;top:467px;width:376px;text-align:center;font-size:7px;font-weight:700;color:var(--green-dark)}

/* cover */
.cover-kicker{position:absolute;left:157px;top:44px;font-family:"Open Sans",Arial,sans-serif;font-weight:300;font-size:14px;color:var(--green-mid);line-height:1}
.cover-higher{position:absolute;left:154px;top:56px;font-family:"Open Sans",Arial,sans-serif;font-weight:300;font-size:41px;letter-spacing:-1.5px;color:var(--green-mid);line-height:1}
.cover-commission{position:absolute;left:264px;top:75px;font-family:"Open Sans",Arial,sans-serif;font-weight:300;font-size:12px;color:var(--green-mid);line-height:1}
.cover-levels{position:absolute;left:267px;top:84px;font-family:"Open Sans",Arial,sans-serif;font-weight:300;font-size:19px;color:var(--green-mid);line-height:1}
.cover-scene{position:absolute;left:0;top:166px;width:376px;height:202px;background:radial-gradient(ellipse at 55% 45%,#ffffff 0%,#e7e8e7 55%,#bfc1bf 100%)}
.cover-band{position:absolute;left:0;top:368px;width:376px;height:30px;background:var(--green-pale)}
.cover-url-box{position:absolute;left:257px;top:368px;width:119px;height:30px;background:var(--green-mid);color:#fff;font-size:6.4px;padding:11px 0 0 12px}
</style>
</head>
<body>
<div class="set-title">Tri-fold brochure option 2 set</div>

<section class="panel panel-page5">
  <div class="header-tab"></div><div class="header-band"></div>
  <div class="header-num">1</div>
  <h1 class="header-title">PROPERTY</h1>
  <p class="header-sub">7 different ways to market</p>

  <h2 class="sec-head" style="left:23px;top:98px">3D Floor Plan</h2>
  <p class="copy" style="left:23px;top:110px;width:216px">The most sophisticated plans, 3D artist impressions, are generated from details building plans by special 3D software, and used for bringing yet-to-be-built properties to life in a highly realistic fashion.</p>
  <div class="media" role="img" aria-label="3D rendered floor plan of a furnished home" style="left:256px;top:89px;width:97px;height:82px;background:linear-gradient(135deg,#d9cbb6,#9b8062 50%,#5d4a38)"></div>
  <ul class="price-list" style="left:23px;top:149px"><li>1 - 2 Bedroom $___</li><li>3 - 4 Bedroom $___</li><li>5 - 6 Bedroom $___</li></ul>
  <p class="large-homes" style="left:23px;top:189px">Large Homes (600sqm +) $___</p>

  <h2 class="sec-head" style="left:23px;top:216px">3D Walkthroughs</h2>
  <ul class="price-list" style="left:23px;top:230px"><li>BLA BLA BLA</li><li>1 - 2 Bedroom $___</li><li>3 - 4 Bedroom $___</li><li>5 - 6 Bedroom $___</li></ul>
  <p class="large-homes" style="left:21px;top:281px">Large Homes (600sqm +) $___</p>
  <div class="video-frame"><div class="media" role="img" aria-label="Walkthrough still of a furnished living room"></div></div>
  <p class="hyper-note">HYPER LINK<br>TO WALK THROUGH<br>+ PICTURE</p>

  <h2 class="sec-head" style="left:23px;top:308px">Furniture Layout</h2>
  <p class="copy" style="left:23px;top:322px;width:308px">Want to showcase a new development or vacant property. We can also embed the floor plan on your website and allow buyers to explore the floor plan, decorate it, and get a real feel for their potential new home.</p>
  <ul class="price-list" style="left:23px;top:362px"><li>1 - 2 Bedroom $___</li><li>3 - 4 Bedroom $___</li><li>5 - 6 Bedroom $___</li></ul>
  <p class="large-homes" style="left:126px;top:381px">Large Homes (600sqm +) $___</p>

  <div class="photo-strip" role="img" aria-label="Strip of styled interior photographs: lounge, dining, kitchen"></div>
  <div class="footer-band"></div>
  <div class="footer-url-box">www.roomharbourly.com.au</div>
  <div class="footer-rule"></div>
</section>

<section class="panel panel-back">
  <div class="header-tab"></div><div class="header-band"></div>
  <div class="header-num">1</div>
  <h1 class="header-title">PROPERTY</h1>
  <p class="header-sub">7 different ways to market</p>

  <p class="sec-head title-case" style="left:26px;top:88px;width:320px">For an extra $_____ per month we include an interactive plans to everyone of your agencies floor plans</p>
  <h2 class="sec-head" style="left:26px;top:113px">Interactive Floor Plans</h2>
  <p class="copy" style="left:26px;top:124px;width:324px">Interactive floor plans are designed to engage buyers with your professional photography and a realistic plan of your listing. We know that your website is the centre of your online marketing strategy, so we can embed every floor plan on your website and this interactivity enhances the viewing experience and motivates buyers to take action.</p>
  <h2 class="sec-head title-case" style="left:26px;top:168px">2D Floor Plans</h2>
  <p class="copy" style="left:26px;top:180px;width:324px">Allow buyers to view plans on their mobile devices in either choice of black and white or coloured.<br>Allow potential buyers to explore the floor plan, decorate it, and get a real feel for their new home</p>
  <h2 class="sec-head title-case" style="left:26px;top:208px">Interactive Floor Plans</h2>
  <p class="copy" style="left:26px;top:223px;width:324px">Compliment your professional photography and allow buyers to virtually inspect their property 24/7.</p>
  <h2 class="sec-head title-case" style="left:26px;top:239px">Agency Branding</h2>
  <p class="copy" style="left:26px;top:252px;width:324px">Brand your Interactive Floor Plans in your company's own style, adding your own logo and company colours.</p>

  <div class="offer-band">It's more than a floor plan. We this subscriptions you can engage your customers with a richer information. You can add all the detail needed to best represent your listing.</div>
  <p class="plan-link">http://fp.link/r7kq2m</p>
  <p class="book-cta">Book a Floor Plan online before the end of<br>October and we will include a site plan for Free!</p>
  <div class="help-band">We can help you improve your end sales result?</div>
  <div class="phone-band">Ph: 0412 555 270 | www.roomharbourly.com.au</div>
  <div class="brand" style="left:128px;top:446px"><span class="brand-square"></span><span class="brand-name">roomharbourly</span></div>
  <p class="brand-url">www.roomharbourly.com.au</p>
</section>

<section class="panel panel-cover">
  <p class="cover-kicker">Want to achieve</p>
  <h1 class="cover-higher">Higher</h1>
  <span class="cover-commission">commission</span>
  <span class="cover-levels">levels?</span>
  <div class="cover-scene" role="img" aria-label="3D house model rising from a floor plan beside a businessman holding rolled plans"></div>
  <div class="cover-band"></div>
  <div class="cover-url-box">www.roomharbourly.com.au</div>
  <div class="brand" style="left:202px;top:480px"><span class="brand-square"></span><span class="brand-name">roomharbourly</span></div>
</section>

<p class="page-label" style="left:56px">Page 5</p>
<p class="page-label" style="left:446px">Back Page 6</p>
<p class="page-label" style="left:820px">Front Cover Page 1</p>
</body>
</html>
```